Redesign for existing homepage

We would like a redesign for our websites 2 column homepage
We provide engine repair and reconditioning services
We would like a cleaner, modern site that works well with our logo colors
Please see the attached brief for more info
Target Market(s)
25 - 45
Industry/Entity Type
Cleaner
Requirements
Must have
- Google Fonts

```html
<!DOCTYPE html>
<html lang="en">
<head>
<meta charset="utf-8">
<title>Harlow Engine Reconditioners</title>
<link rel="stylesheet" href="https://fonts.googleapis.com/css2?family=Cabin:wght@400;500;600;700&display=swap">
<style>
:root{
  --blue:#2184cc;
  --blue-dark:#1a6fae;
  --blue-light:#6cc3f2;
  --heading-blue:#2a8ed0;
  --ink:#2b2b2b;
  --muted:#555;
  --white:#fff;
  --rule:#1d1d1d;
}
*{box-sizing:border-box;margin:0;padding:0}
html,body{width:1200px;height:1196px;overflow:hidden}
body{position:relative;background:var(--white);font-family:"Cabin",sans-serif;color:var(--ink)}
.top-bar{position:absolute;left:0;top:0;width:1200px;height:10px;background:var(--blue)}
.brand{position:absolute;left:206px;top:56px;display:flex;align-items:center;gap:12px;font-size:34px;font-weight:700;color:var(--blue)}
.brand-dot{width:28px;height:28px;border-radius:50%;background:var(--blue)}
.contact-phone{position:absolute;left:763px;top:42px;font-size:22px;color:#444;display:flex;align-items:center;gap:6px}
.contact-address{position:absolute;left:820px;top:90px;font-size:16px;line-height:20px;color:#444;display:flex;gap:12px;align-items:center}
.header-rule{position:absolute;left:0;top:164px;width:1200px;height:4px;background:var(--rule)}
.hero{position:absolute;left:0;top:168px;width:1200px;height:433px;
  background:linear-gradient(100deg,#5a1d1c 0%,#8e3a33 30%,#b9b3ad 58%,#d9d6d2 75%,#8a8680 100%)}
.nav{position:absolute;left:210px;top:165px;height:59px;display:flex;background:var(--blue);z-index:2}
.nav a{display:flex;align-items:center;justify-content:center;height:59px;color:var(--white);text-decoration:none;font-size:17.5px;font-weight:500;text-transform:uppercase;border-right:1px solid var(--blue-dark);letter-spacing:-.2px}
.nav .home{width:56px;background:var(--blue-light)}
.hero-title{position:absolute;left:221px;font-weight:400;background:var(--white);color:#111;padding:0 10px;white-space:nowrap}
.hero-title.small{top:351px;height:48px;font-size:35px;line-height:48px;width:270px}
.hero-title.large{top:408px;height:65px;font-size:45px;line-height:65px;width:462px}
.slider-arrows{position:absolute;left:915px;top:552px;width:74px;height:49px;background:var(--blue-light);display:flex;align-items:center;justify-content:center}
.features-bg{position:absolute;left:0;top:601px;width:1200px;height:100px;background:linear-gradient(#e6e6e6,#fff)}
.feature{position:absolute;top:615px;width:240px}
.feature h2{font-size:23.5px;font-weight:500;line-height:31px;color:var(--heading-blue);height:65px;letter-spacing:-.3px}
.feature-photo{width:231px;height:122px;background:linear-gradient(90deg,#d8d8d8,#6d6d6d)}
.feature-photo.oil{background:linear-gradient(90deg,#2a2a2a,#c8a04a 50%,#1e1e1e)}
.feature p{margin-top:13px;font-size:14px;line-height:18px;color:var(--muted);width:236px}
.btn{margin-top:10px;display:flex;width:170px;height:30px;background:var(--blue-light);color:var(--white);text-decoration:none;font-size:15px;font-weight:600}
.btn span{flex:1;padding-left:10px;line-height:30px}
.btn i{width:30px;background:var(--blue);display:flex;align-items:center;justify-content:center}
.map{position:absolute;left:0;top:966px;width:1200px;height:184px;background:linear-gradient(90deg,#efe9dc,#e8e3d6 40%,#9ec4e6 48%,#efe9dc 60%,#eae5d8)}
.footer{position:absolute;left:0;top:1150px;width:1200px;height:46px;background:var(--blue)}
.footer-note{position:absolute;left:211px;top:17px;font-size:10px;color:#cfe6f7}
.footer-note b{color:var(--white)}
.social{position:absolute;left:882px;top:12px;display:flex;gap:9px}
.social span{width:22px;height:22px;border-radius:50%;background:#5a9fd3}
.social span:first-child{background:var(--blue-light)}
</style>
</head>
<body>
<div class="top-bar"></div>
<header>
  <div class="brand"><span class="brand-dot"></span>Harlow Engine Reconditioners</div>
  <div class="contact-phone">
    <svg width="20" height="26" viewBox="0 0 20 26"><path d="M4 2 L8 1 L10 8 L7 10 Q9 16 13 19 L16 17 L19 23 L15 25 Q6 22 3 10 Z" fill="#888"/></svg>
    Petone: (04) 555 0142
  </div>
  <div class="contact-address">
    <svg width="20" height="30" viewBox="0 0 20 30"><path d="M10 1 A9 9 0 0 1 19 10 C19 17 10 29 10 29 C10 29 1 17 1 10 A9 9 0 0 1 10 1Z" fill="#888"/><circle cx="10" cy="10" r="3.5" fill="#fff"/></svg>
    <span>82 Ferrier Street<br>Petone, Wellington.</span>
  </div>
</header>
<div class="header-rule"></div>
<section class="hero" role="img" aria-label="Mechanic working under a car raised on a vehicle lift"></section>
<nav class="nav">
  <a class="home" href="#"><svg width="22" height="20" viewBox="0 0 22 20"><path d="M11 1 L21 10 H18 V19 H13 V13 H9 V19 H4 V10 H1 Z" fill="#fff"/></svg></a>
  <a href="#" style="width:97px">About us</a>
  <a href="#" style="width:158px">Service &amp; Repair</a>
  <a href="#" style="width:181px">Trade Costumers</a>
  <a href="#" style="width:128px">Car Engines</a>
  <a href="#" style="width:135px;border-right:0">Contact us</a>
</nav>
<h1>
  <span class="hero-title small">Specialist engine</span>
  <span class="hero-title large">Repair &amp; Reconditioning</span>
</h1>
<div class="slider-arrows">
  <svg width="50" height="26" viewBox="0 0 50 26"><path d="M18 3 L8 13 L18 23" stroke="#fff" stroke-width="4" fill="none"/><path d="M32 3 L42 13 L32 23" stroke="#1d6aa8" stroke-width="4" fill="none"/></svg>
</div>
<div class="features-bg"></div>
<section class="feature" style="left:223px">
  <h2>Need service and repair for a private vehicle?</h2>
  <div class="feature-photo" role="img" aria-label="Hand holding a spanner over an engine"></div>
  <p>Get an efficient and honest diagnosis, along with repair work that will have your car running smoothly.</p>
  <a class="btn" href="#"><span>Make an Enquiry</span><i><svg width="10" height="14" viewBox="0 0 10 14"><path d="M2 2 L8 7 L2 12" stroke="#fff" stroke-width="2.5" fill="none"/></svg></i></a>
</section>
<section class="feature" style="left:494px">
  <h2>Interested in becoming a trade customer?</h2>
  <div class="feature-photo oil" role="img" aria-label="Engine oil being poured into an engine"></div>
  <p>You can outsource your the specialist machining jobs to us at very competitive rates.</p>
  <a class="btn" href="#"><span>Trade Costumers</span><i><svg width="10" height="14" viewBox="0 0 10 14"><path d="M2 2 L8 7 L2 12" stroke="#fff" stroke-width="2.5" fill="none"/></svg></i></a>
</section>
<section class="feature" style="left:759px">
  <h2>Is your classic or race car your passion?</h2>
  <div class="feature-photo oil" role="img" aria-label="Oil poured into a car engine bay"></div>
  <p>Get an efficient and honest diagnosis, along with repair work that will have your car running smoothly.</p>
  <a class="btn" href="#"><span>Contact Us</span><i><svg width="10" height="14" viewBox="0 0 10 14"><path d="M2 2 L8 7 L2 12" stroke="#fff" stroke-width="2.5" fill="none"/></svg></i></a>
</section>
<div class="map" role="img" aria-label="Street map showing the workshop location"></div>
<footer class="footer">
  <p class="footer-note"><b>CAR REPAIR</b> © 2014 | Privacy Policy</p>
  <div class="social"><span></span><span></span><span></span><span></span></div>
</footer>
</body>
</html>
```